Dental marketing ad poster

I recently opened a new dental practice about 2 months ago and would like to have an ad designed for an A-frame poster to place outside our office. The goal of this ad is to attract and appeal to potential patients so they feel encouraged to come into the practice.
I’m leaving the creative direction up to you—I’d like to see what you can come up with. The ad can be funny or serious, but it should be eye-catching and patient-focused. Please highlight that we provide crowns, implants and teeth whitening.
My theme color is green but I’ll accept any color
Let me see your ideas!
Dentistry

```html
<!DOCTYPE html>
<html lang="en">
<head>
<meta charset="utf-8">
<title>Willowmere Dentistry – A-frame Poster</title>
<link href="https://fonts.googleapis.com/css2?family=Barlow+Condensed:wght@400;500;600;700&family=Libre+Caslon+Text:wght@400&display=swap" rel="stylesheet">
<style>
  :root{
    --stage:#2f3936;
    --paper:#ffffff;
    --green:#1a9a4a;
    --mint:#dcefe3;
    --mint-soft:#e6f3ea;
    --mint-deep:#a9dcbc;
    --ink:#111111;
    --card:#f3f3f3;
    --rule:#e2e2e2;
  }
  *{margin:0;padding:0;box-sizing:border-box}
  html,body{width:1200px;height:675px;overflow:hidden;background:var(--stage)}
  .poster{position:absolute;left:386px;top:35px;width:428px;height:605px;background:var(--paper);font-family:"Barlow Condensed",sans-serif;color:var(--ink)}
  .hero{position:absolute;left:21px;top:0;width:386px;height:282px;border-radius:0 0 8px 8px;overflow:hidden;
    background:linear-gradient(160deg,var(--mint-soft) 0%,#d5ede0 60%,var(--mint-deep) 100%)}
  .hero-photo{position:absolute;right:0;top:33px;width:199px;height:249px;
    background:radial-gradient(ellipse at 58% 35%,#d9b49a 0%,#c9a08a 28%,rgba(210,222,214,.9) 55%,rgba(255,255,255,0) 75%),
               linear-gradient(180deg,rgba(255,255,255,0) 55%,#f2f2f0 80%)}
  .headline{position:absolute;left:15px;top:44px;font-family:"Libre Caslon Text",serif;font-weight:400;font-size:37px;line-height:36.5px;letter-spacing:-1px}
  .tagline{position:absolute;left:15px;top:211px;font-family:"Libre Caslon Text",serif;font-size:18.5px;line-height:20px;letter-spacing:-.3px}
  .section-title{position:absolute;left:21px;top:292px;width:386px;text-align:center;font-weight:700;font-size:20px;color:var(--green);letter-spacing:.3px}
  .section-title::before,.section-title::after{content:"";position:absolute;top:50%;width:130px;height:1px;background:var(--rule)}
  .section-title::before{left:0}.section-title::after{right:0}
  .services{position:absolute;left:21px;top:324px;width:386px;height:98px;background:var(--card);border-radius:10px;display:flex;padding:16px 0 0}
  .service{flex:1;text-align:center;border-right:1px solid var(--rule);height:66px}
  .service:last-child{border-right:none}
  .icon{width:29px;height:29px;margin:0 auto 6px;display:block}
  .service-name{font-weight:700;font-size:13.5px;color:var(--green);line-height:16px}
  .service-desc{font-weight:500;font-size:12px;line-height:16px}
  .more-services{position:absolute;left:0;top:426px;width:428px;text-align:center;font-weight:500;font-size:11.5px}
  .more-services .dot{display:inline-block;width:4px;height:4px;border-radius:50%;background:var(--green);margin:0 7px;vertical-align:middle}
  .brand{position:absolute;left:0;top:467px;width:428px;text-align:center;font-family:"Libre Caslon Text",serif;font-size:22px;color:var(--green);letter-spacing:-.3px}
  .walkins{position:absolute;left:0;top:515px;width:428px;height:50px;background:var(--mint);display:flex;align-items:center;justify-content:center;gap:18px;font-size:25px;font-weight:500;letter-spacing:-.4px}
  .walkins .phone{color:var(--green);font-weight:600}
  .footer{position:absolute;left:0;top:565px;width:428px;height:40px;background:var(--green);color:#fff;text-align:center;font-size:11.5px;padding-top:8px}
</style>
</head>
<body>
<main class="poster">
  <section class="hero">
    <div class="hero-photo" role="img" aria-label="Photo of a smiling young woman in a white top"></div>
    <h1 class="headline">Your<br>Healthiest<br>Smile<br>Starts Here</h1>
    <p class="tagline">Experience modern<br>dentistry designed for you</p>
  </section>

  <h2 class="section-title">KEY SERVICES</h2>

  <section class="services">
    <div class="service">
      <svg class="icon" viewBox="0 0 30 30"><circle cx="15" cy="15" r="15" fill="#1a9a4a"/><path d="M15 8l6 2.2v4.3c0 3.8-2.6 6.4-6 7.5-3.4-1.1-6-3.7-6-7.5v-4.3z" fill="none" stroke="#fff" stroke-width="1.2"/><path d="M12.6 13c1-.6 1.6-.2 2.4.2.8-.4 1.4-.8 2.4-.2.8.9.3 2.5-.2 3.6l-.6 1.8-1-1.8-.6 0-1 1.8-.6-1.8c-.5-1.1-1-2.7-.2-3.6z" fill="none" stroke="#fff" stroke-width=".9"/></svg>
      <div class="service-name">CROWNS</div>
      <div class="service-desc">Restore &amp; Protect</div>
    </div>
    <div class="service">
      <svg class="icon" viewBox="0 0 30 30"><circle cx="15" cy="15" r="15" fill="#1a9a4a"/><path d="M10.5 9.5c1.8-1 3-.3 4.5.4 1.5-.7 2.7-1.4 4.5-.4 1.6 1.6.8 4.6-.2 6.7l-1.2 5-1.6-4.2h-3l-1.6 4.2-1.2-5c-1-2.1-1.8-5.1-.2-6.7z" fill="none" stroke="#fff" stroke-width="1.2"/><path d="M21 6.5v3M19.5 8h3" stroke="#fff" stroke-width="1"/></svg>
      <div class="service-name">IMPLANTS</div>
      <div class="service-desc">Permanent Solutions</div>
    </div>
    <div class="service">
      <svg class="icon" viewBox="0 0 30 30"><circle cx="15" cy="15" r="15" fill="#1a9a4a"/><path d="M15 7v16M7 15h16M9.5 9.5l11 11M20.5 9.5l-11 11" stroke="#fff" stroke-width="1.1"/><circle cx="15" cy="15" r="2.4" fill="#1a9a4a" stroke="#fff" stroke-width="1"/></svg>
      <div class="service-name">WHITENING</div>
      <div class="service-desc">Dazzling Brightness</div>
    </div>
  </section>

  <p class="more-services">Hygiene &amp; Cleanings<span class="dot"></span>Cosmetic Dentistry<span class="dot"></span>Dentures &amp; Partials<span class="dot"></span>Emergency Services</p>

  <div class="brand">Willowmere Dentistry</div>

  <div class="walkins"><span>Walk-ins Welcome!</span><span class="phone">(555) 314-2680</span></div>
  <footer class="footer">hello@willowmeredental.com</footer>
</main>
</body>
</html>
```